Ein Cover für den KALTSPIEGEL!
Taloma ist wirklich eine Elite-Designerin mit ungewöhnlichen, smarten Ideen. Die Zusammenarbeit war perfekt und die Entwürfe kamen ultraschnell. So hat mir mein Projekt viel Spaß gmemacht. Das Ergebnis ist sehenswert - ich hätte mir kein schöneres Cover für mein Buch vorstellen können. Tausend Dank, Taloma :-)
Zielgruppe
Zielgruppe sind Leser, die in Spannung versetzt und in die Geschichte hineingesogen werden. Detektivroman mit Action.
Aufgabenstellung
Buchtitel: „KALTSPIEGEL“
Schrift: sehr groß, Blockschrift, in fetten, serifenlosen Lettern, bedrohlich, aber zeitgemäß. Soll mindestens ein Drittel des Covers einnehmen.
Name der Autorin: HELKE DORMANN, ebenfalls groß und Blockschrift.
Genre: Krimi, in unauffälliger Schriftgröße.
Der Inhalt des Kaltspiegel bietet mindestens drei Themen für die Covergestaltung:
Entweder:
- Ein Reiter, der (laut einer für den Inhalt relevanten Legende) über den stürmischen Nachthimmel reitet, wild und verzweifelt, mit erhobenem Schwert.
Er könnte auch, wie im Dateiupload "Bertold", aus einer Verpackung herausspringen oder daraus zu sehen sein.
Oder:
- Novembertag, dementsprechend kahle Bäume, eine Hütte am Weiher, alt und heruntergekommen, Tür hängt aus den Angeln, darin ein Tisch, auf dem eine Leiche wie aufgebahrt liegt, vielleicht angeleuchtet von nicht sichtbarer Quelle.
Hintergrund dunkel, das Ganze vielleicht verschwommen, wie im Traum.
- Die Leiche einer jungen Frau (18 Jahre alt) auf einem Schulhof, sie ist vom Schuldach gestoßen worden und liegt auf dem Waschbeton. Hintergrund hell, weiß oder cremeweiß. Die Leiche soll in die Schrift eingebettet sein, falls möglich, wie in einigen der Dateiuploads.
Thema vorwiegend düster. Fokus auf ein einzelnes Objekt im Bild. Klare, düstere, dramatische und spannende Botschaft, leicht zu verstehen. Möglichst nur ein Objekt auf dem Bild.

```html
<!DOCTYPE html>
<html lang="de">
<head>
<meta charset="utf-8">
<title>Kaltspiegel – Helke Dormann</title>
<link rel="stylesheet" href="https://fonts.googleapis.com/css2?family=Anton&family=Open+Sans:wght@400&display=swap">
<style>
  :root {
    --paper: #f4f4f4;
    --paper-shade: #d9d9d9;
    --blood: #d40a0a;
    --blood-deep: #8e0000;
    --ink: #140000;
    --genre-ink: #1c1c1c;
  }
  html, body {
    margin: 0;
    padding: 0;
    overflow: hidden;
    background: var(--paper);
  }
  .cover {
    position: relative;
    width: 750px;
    height: 1200px;
    overflow: hidden;
    background:
      radial-gradient(ellipse 90% 70% at 50% 55%, var(--paper-shade) 0%, #ececec 60%, #fafafa 100%);
  }
  .cover-art {
    position: absolute;
    inset: 0;
  }
  .author, .title {
    font-family: "Anton", "Oswald", sans-serif;
  }
  .genre {
    position: absolute;
    left: 0;
    right: 0;
    top: 940px;
    margin: 0;
    text-align: center;
    font-family: "Open Sans", Arial, sans-serif;
    font-size: 50px;
    font-weight: 400;
    line-height: 60px;
    color: var(--genre-ink);
  }
</style>
</head>
<body>
<div class="cover">
  <svg class="cover-art" width="750" height="1200" viewBox="0 0 750 1200" xmlns="http://www.w3.org/2000/svg">
    <defs>
      <linearGradient id="author-fill" x1="0" y1="0" x2="1" y2="0.3">
        <stop offset="0" stop-color="var(--blood-deep)"/>
        <stop offset="0.45" stop-color="#5a0000"/>
        <stop offset="1" stop-color="var(--ink)"/>
      </linearGradient>
      <linearGradient id="title-fill" x1="0" y1="0" x2="0" y2="1">
        <stop offset="0" stop-color="#e00d0d"/>
        <stop offset="1" stop-color="#b80404"/>
      </linearGradient>
      <linearGradient id="photo-tone" x1="0" y1="0" x2="0" y2="1">
        <stop offset="0" stop-color="#d40808"/>
        <stop offset="0.35" stop-color="#b00000"/>
        <stop offset="0.6" stop-color="#2a0a0a"/>
        <stop offset="1" stop-color="#1a1a1a"/>
      </linearGradient>
    </defs>

    <g class="victim-photo" role="img" aria-label="Fotografie: junge Frau mit rotem Haar in rot-schwarzem Kleid, gestürzt auf hellem Waschbeton liegend, rotes Tuch ausgebreitet">
      <rect x="170" y="370" width="580" height="548" rx="28" fill="url(#photo-tone)" opacity="0.88"/>
    </g>

    <text class="author" x="55" y="240" font-size="125" textLength="640" lengthAdjust="spacingAndGlyphs" fill="url(#author-fill)">HELKE DORMANN</text>

    <text class="title title-line-1" x="30" y="676" font-size="197" textLength="311" lengthAdjust="spacingAndGlyphs" fill="url(#title-fill)">KALT</text>
    <text class="title title-line-2" x="303" y="867" font-size="193" textLength="419" lengthAdjust="spacingAndGlyphs" fill="url(#title-fill)">SPIEGEL</text>
  </svg>

  <p class="genre">Krimi</p>
</div>
</body>
</html>
```